Divorce Lawyer print and ebook cover (Lanterns over the quiet harbor )

I need a front and back cover for my divorce and family law book. I already have a photo and title. The back cover photo is not necessary but can be interesting the Front-main cover is a must

Target Market(s)

Prospective client

Colors

Designer to choose colors to be used in the design.

Requirements
Must have
• Front photo by viewable.

```html
<!DOCTYPE html>
<html lang="en">
<head>
<meta charset="utf-8">
<title>Lanterns over the quiet harbor — cover wrap</title>
<link href="https://fonts.googleapis.com/css2?family=Oswald:wght@500;600;700&family=Barlow+Condensed:wght@500;600;700&family=Roboto+Mono:wght@400;700&display=swap" rel="stylesheet">
<style>
  :root {
    --page-bg: #e9e9e7;
    --ink-dark: #0d1216;
    --ink-deep: #141c22;
    --fog-blue: #8fa3ae;
    --fog-light: #c9d3d6;
    --meadow: #cdd678;
    --amber: #f0b400;
    --white: #ffffff;
    --body-text: #e6e9eb;
    --portrait-grey: #b8bcbf;
  }
  * { margin: 0; padding: 0; box-sizing: border-box; }
  html, body {
    width: 1200px; height: 3188px; overflow: hidden;
    background: var(--page-bg);
  }
  .cover-wrap {
    position: absolute; left: 5px; top: 1184px;
    width: 1190px; height: 820px;
    display: flex;
    box-shadow: 0 10px 30px rgba(0,0,0,.25);
  }

  /* Back cover */
  .back-cover {
    position: relative; width: 546px; height: 100%;
    background: var(--ink-dark); overflow: hidden; color: var(--white);
  }
  .back-photo {
    position: absolute; left: 0; top: 0; width: 100%; height: 330px;
    background: linear-gradient(180deg, #6f7a78 0%, #8a8068 45%, #5b5648 70%, var(--ink-dark) 100%);
  }
  .back-title {
    position: absolute; left: 0; right: 0; top: 270px;
    text-align: center;
    font: 600 36px/44px "Barlow Condensed", sans-serif;
    letter-spacing: 3px; text-transform: uppercase;
  }
  .accent { color: var(--amber); }
  .back-blurb {
    position: absolute; left: 58px; right: 58px; top: 362px;
    text-align: center; color: var(--body-text);
    font: 400 14.5px/19.5px "Roboto Mono", monospace;
  }
  .back-blurb b, .bio-text b { font-weight: 700; }
  .author-portrait {
    position: absolute; left: 30px; top: 552px; width: 138px; height: 128px;
    background: linear-gradient(180deg, #d6d9db, var(--portrait-grey));
  }
  .bio-text {
    position: absolute; left: 182px; top: 552px; width: 330px;
    color: var(--body-text);
    font: 400 11px/15.5px "Roboto Mono", monospace;
  }
  .barcode-box {
    position: absolute; left: 376px; top: 702px; width: 132px; height: 92px;
    background: var(--white);
  }

  /* Spine */
  .spine {
    position: relative; width: 66px; height: 100%;
    background: linear-gradient(180deg, #5f6c73 0%, #2e383e 45%, var(--ink-deep) 100%);
    overflow: hidden;
  }
  .spine-text {
    position: absolute; left: 33px; top: 62px;
    transform-origin: 0 0; transform: rotate(90deg) translateY(-50%);
    white-space: nowrap; display: flex; align-items: baseline; gap: 28px;
    color: var(--white);
  }
  .spine-title { font: 700 25px/1 "Barlow Condensed", sans-serif; letter-spacing: 4px; text-transform: uppercase; }
  .spine-author { font: 600 13px/1 "Barlow Condensed", sans-serif; letter-spacing: 4px; text-transform: uppercase; }

  /* Front cover */
  .front-cover { position: relative; width: 578px; height: 100%; overflow: hidden; }
  .front-photo {
    position: absolute; inset: 0;
    background:
      radial-gradient(ellipse 60% 45% at 95% 10%, var(--meadow), rgba(205,214,120,0) 70%),
      linear-gradient(180deg, var(--fog-light) 0%, var(--fog-blue) 35%, #55646c 60%, #2a343a 80%, var(--ink-deep) 100%);
  }
  .front-title {
    position: absolute; right: 26px; top: 462px;
    color: var(--white);
    font: 600 100px/1 "Oswald", sans-serif; letter-spacing: 1px;
    text-transform: uppercase; white-space: nowrap;
  }
  .front-subtitle {
    position: absolute; right: 34px; top: 576px;
    color: var(--white);
    font: 600 38px/1 "Barlow Condensed", sans-serif; letter-spacing: 3px;
    text-transform: uppercase; white-space: nowrap;
  }
  .front-author {
    position: absolute; left: 0; right: 0; top: 758px; padding-left: 40px;
    text-align: center; color: var(--white);
    font: 700 33px/1 "Barlow Condensed", sans-serif; letter-spacing: 8px;
    text-transform: uppercase;
  }
</style>
</head>
<body>
  <main class="cover-wrap">
    <section class="back-cover">
      <div class="back-photo" role="img" aria-label="Photo of a toddler in a knitted blue hat on a playground swing, held by a parent's hands"></div>
      <h2 class="back-title">Lanterns over<br>the <span class="accent">quiet harbor</span></h2>
      <p class="back-blurb">Lorem ipsum dolor sit amet, consectetur adipisc-ing elit. Vivamus vel sapien vel urna commodo porttitor. Praesent id turpis a augue ultrices auctor. Pellentesque mollis, enim eget condimen-tum dictum, nulla erat malesuada tortor, interdum tempus tortor lectus nec tellus. Etiam eget pel-lentesque ligula, <b class="accent">ac maximus nibh.</b></p>
      <div class="author-portrait" role="img" aria-label="Author portrait placeholder"></div>
      <p class="bio-text">Lorem ipsum dolor sit amet, consectetur adipisc-ing elit. Vivamus vel sapien vel urna commodo porttitor. Praesent id turpis a augue ultrices auctor. Pellentesque mollis, enim eget condimen-tum dictum, nulla erat malesuada tortor, inter-dum tempus tortor lectus nec tellus. Etiam eget pellentesque ligula, <b>ac maximus nibh.</b></p>
      <div class="barcode-box" aria-hidden="true"></div>
    </section>

    <section class="spine">
      <div class="spine-text">
        <span class="spine-title">Lanterns over the <span class="accent">quiet harbor</span></span>
        <span class="spine-author">Author Name</span>
      </div>
    </section>

    <section class="front-cover">
      <div class="front-photo" role="img" aria-label="Photo of a man in a dark suit seen from behind on a foggy forest road, beside a yellow signpost pointing to Old Life and New Life"></div>
      <h1 class="front-title">Lanterns</h1>
      <p class="front-subtitle">Over the <span class="accent">quiet harbor</span></p>
      <p class="front-author">Author Name</p>
    </section>
  </main>
</body>
</html>
```